Halvorn spray foam and Environmental

I have business cards but need new ones. The ones I have are very bland. Here is. Y company website http://www.halvornsprayfoam.ca

Also I can send you copies of the current cards
I would also need my current logo on the new design as well.. Also spray foam and Environmental

Industry/Entity Type

Business

Logo Text

Halvorn.

```html
<!DOCTYPE html>
<html lang="en">
<head>
<meta charset="utf-8">
<title>Halvorn business cards</title>
<link href="https://fonts.googleapis.com/css2?family=Roboto:wght@400;500;700&display=swap" rel="stylesheet">
<style>
  :root {
    --bg: #2b2b2b;
    --purple: #5b2568;
    --paper: #f1f1f1;
    --ink-light: #ffffff;
  }
  * { box-sizing: border-box; margin: 0; padding: 0; }
  html, body { width: 1200px; height: 960px; overflow: hidden; }
  body {
    background: var(--bg);
    font-family: "Roboto", Arial, sans-serif;
    position: relative;
  }
  .card {
    position: absolute;
    width: 600px;
    height: 343px;
    background: var(--purple);
    box-shadow: 0 2px 6px rgba(0,0,0,.45);
    overflow: hidden;
  }
  .card--foam { left: 314px; top: 113px; }
  .card--enviro { left: 311px; top: 472px; background: var(--paper); }
  .card__shape { position: absolute; inset: 0; width: 600px; height: 343px; }
  .card__shape .paper { fill: var(--paper); }
  .card__shape .band { fill: var(--purple); }

  .details {
    position: absolute;
    color: var(--ink-light);
    top: 59px;
  }
  .card--foam .details { left: 30px; text-align: left; }
  .card--enviro .details { right: 25px; text-align: right; top: 62px; }
  .details__name { font-size: 20px; font-weight: 500; line-height: 24px; }
  .details__role { font-size: 15px; font-weight: 400; line-height: 22px; }
  .details__division { font-size: 19px; font-weight: 700; line-height: 24px; margin-top: 10px; }
  .details__services { font-size: 15px; line-height: 18px; margin-top: 4px; }
  .contact { list-style: none; margin-top: 5px; font-size: 14.5px; }
  .contact li { display: flex; align-items: center; gap: 9px; height: 19.5px; }
  .card--enviro .contact li { justify-content: flex-end; }
  .contact svg { width: 13px; height: 13px; fill: var(--ink-light); flex: none; }

  .brand {
    position: absolute;
    display: flex;
    flex-direction: column;
    align-items: center;
  }
  .card--foam .brand { left: 328px; top: 103px; width: 245px; }
  .card--enviro .brand { left: 30px; top: 109px; width: 240px; }
  .brand__mark { width: 97px; height: 80px; background: var(--purple); }
  .brand__name {
    font-size: 50px;
    font-weight: 700;
    color: var(--purple);
    line-height: 1;
    margin-top: 10px;
  }
</style>
</head>
<body>

<section class="card card--foam" aria-label="Spray foam business card">
  <svg class="card__shape" viewBox="0 0 600 343" aria-hidden="true">
    <path class="paper" d="M326,0 Q254,175 334,343 L600,343 L600,0 Z"/>
    <path class="paper" d="M322,0 Q268,120 280,272 Q262,125 314,0 Z"/>
  </svg>
  <div class="details">
    <p class="details__name">ERIK DAHL</p>
    <p class="details__role">CEO/FOUNDER</p>
    <p class="details__division">Spray Foam</p>
    <p class="details__services">Roofing Foam, Slabjacking<br>2 pound / Half pound<br>Sound Proofing, Batt insulation<br>Attic Blow in</p>
    <ul class="contact">
      <li><svg viewBox="0 0 16 16"><path d="M3.5 1l2.5 3-1.5 2a9 9 0 0 0 5 5l2-1.5 3 2.5-1.5 2.5C7 15 1 9 1 2.5z"/></svg>604-555-0148</li>
      <li><svg viewBox="0 0 16 16"><path d="M1 4h14v9H1z M1 4l7 5 7-5" fill="none" stroke="#fff" stroke-width="1.6"/></svg>halvornfoam@mailbox.ca</li>
      <li><svg viewBox="0 0 16 16"><circle cx="8" cy="8" r="7"/><path d="M4 5h4v3H5zM9 10h3l-1 3-2-1z" fill="#5b2568"/></svg>www.halvornsprayfoam.ca</li>
    </ul>
  </div>
  <div class="brand">
    <div class="brand__mark"></div>
    <p class="brand__name">HALVORN</p>
  </div>
</section>

<section class="card card--enviro" aria-label="Environmental business card">
  <svg class="card__shape" viewBox="0 0 600 343" aria-hidden="true">
    <path class="band" d="M278,0 Q345,170 265,343 L600,343 L600,0 Z"/>
    <path class="paper" d="M272,0 Q318,130 318,268 Q312,130 280,0 Z"/>
  </svg>
  <div class="brand">
    <div class="brand__mark"></div>
    <p class="brand__name">HALVORN</p>
  </div>
  <div class="details">
    <p class="details__name">ERIK DAHL</p>
    <p class="details__role">CEO/FOUNDER</p>
    <p class="details__division">Environmental</p>
    <p class="details__services">air monitoring, Asbestos testing<br>Asbestos Removal<br>Building Demolition<br>Lead Testing, Mould Removal</p>
    <ul class="contact">
      <li>604-555-0172<svg viewBox="0 0 16 16"><path d="M3.5 1l2.5 3-1.5 2a9 9 0 0 0 5 5l2-1.5 3 2.5-1.5 2.5C7 15 1 9 1 2.5z"/></svg></li>
      <li>halvornenviro@mailbox.ca<svg viewBox="0 0 16 16"><path d="M1 4h14v9H1z M1 4l7 5 7-5" fill="none" stroke="#fff" stroke-width="1.6"/></svg></li>
      <li>www.halvornenvironmental.ca<svg viewBox="0 0 16 16"><circle cx="8" cy="8" r="7"/><path d="M4 5h4v3H5zM9 10h3l-1 3-2-1z" fill="#5b2568"/></svg></li>
    </ul>
  </div>
</section>

</body>
</html>
```